Electrical needs letterhead design

Need a letterhead design for an electrical company. Using the same colours as to what are used in the logo.
After a modern design.

Want the logo in top right or top left.

Must include...

ABN 71 804 239 356
PHONE 0458203917
www.kelmaroo.com.au
jed@kelmaroo.com.au

'ABN' and 'PHONE' in bold.

Keep it basic. Logo top left, details either next to it or far right corner. Dont want any other objects included.

Electrical

```html
<!DOCTYPE html>
<html lang="en">
<head>
<meta charset="utf-8">
<title>Kelmaroo Letterhead</title>
<link rel="stylesheet" href="https://fonts.googleapis.com/css2?family=Arimo:wght@400;700&display=swap">
<style>
  :root {
    --backdrop: #e6e6e6;
    --paper: #ffffff;
    --brand-red: #e0432f;
    --brand-dark: #8e1b16;
    --tint: #f8dad6;
    --bar: #6b6b6b;
    --ink: #1a1a1a;
    --muted: #6f6f6f;
  }
  * { margin: 0; padding: 0; box-sizing: border-box; }
  html, body { width: 1200px; height: 1000px; overflow: hidden; }
  body {
    background: var(--backdrop);
    font-family: "Arimo", Arial, sans-serif;
    color: var(--ink);
    position: relative;
  }
  .cover-card {
    position: absolute;
    left: 522px; top: 121px;
    width: 636px; height: 821px;
    background: var(--brand-red);
    overflow: hidden;
  }
  .cover-card .cover-disc {
    position: absolute;
    left: 196px; top: 250px;
    width: 230px; height: 230px;
    border-radius: 50%;
    background: var(--paper);
  }
  .letterhead {
    position: absolute;
    left: 53px; top: 63px;
    width: 637px; height: 820px;
    background: var(--paper);
    border-top: 5px solid var(--bar);
    border-bottom: 5px solid var(--bar);
    overflow: hidden;
  }
  .tint-disc {
    position: absolute;
    border-radius: 50%;
    background: var(--tint);
    opacity: .55;
  }
  .tint-disc.side { left: -110px; top: 20px; width: 240px; height: 240px; }
  .tint-disc.corner { left: 420px; top: 500px; width: 250px; height: 250px; }
  .brand {
    position: absolute;
    left: 112px; top: 50px;
    display: flex; align-items: center; gap: 8px;
  }
  .brand-dot { width: 14px; height: 14px; border-radius: 50%; background: var(--brand-dark); }
  .brand-name { font-size: 28px; font-weight: 400; color: var(--brand-dark); }
  .contact {
    position: absolute;
    left: 403px; top: 83px;
    display: flex; gap: 10px;
    font-size: 6.5px; line-height: 9px; color: var(--muted);
  }
  .contact .company { color: var(--brand-dark); font-weight: 700; }
  .contact .web { color: var(--brand-dark); font-weight: 700; }
  .contact .label { font-weight: 700; color: var(--ink); }
  .contact .gap { height: 9px; }
  .letter {
    position: absolute;
    left: 112px; top: 142px;
    width: 466px;
    font-size: 8.4px; line-height: 11.4px;
  }
  .letter p { margin-bottom: 11.4px; }
  .letter .sender { margin-bottom: 23px; }
  .letter .recipient { margin-bottom: 23px; }
  .letter .greeting { margin-bottom: 23px; }
  .signature {
    width: 150px; height: 56px;
    margin: 8px 0 12px -14px;
    background: linear-gradient(90deg, #f3f3f3, #fafafa);
  }
</style>
</head>
<body>
  <div class="cover-card">
    <div class="cover-disc"></div>
  </div>

  <div class="letterhead">
    <div class="tint-disc side"></div>
    <div class="tint-disc corner"></div>

    <div class="brand">
      <span class="brand-dot"></span>
      <span class="brand-name">Kelmaroo</span>
    </div>

    <div class="contact">
      <div>
        <div class="company">Kelmaroo</div>
        <div>Unit 4, Harlow Court</div>
        <div>58 Millbrook Road</div>
        <div>Eastvale</div>
        <div><span class="label">ABN</span> 71 804 239 356</div>
      </div>
      <div>
        <div><span class="label">PHONE</span> 0458203917</div>
        <div class="gap"></div>
        <div>jed@kelmaroo.com.au</div>
        <div class="web">www.kelmaroo.com.au</div>
      </div>
    </div>

    <div class="letter">
      <p class="sender">Unit 4, Harlow Court<br>58 Millbrook Road, Eastvale<br>09 Aug, 2014</p>
      <p class="recipient">Mr. Sam Carter<br>47 Elm Street<br>Riverton, RC 40210</p>
      <p class="greeting">Dear Mr. Sam Carter,</p>
      <p>Lorem ipsum dolor sit amet, id est natum justo, est possit bonorum voluptatum ei, eos magna contentiones in. Vel singulis neglegentur disputationi te, cu vim aperiri malorum. Ut idque postulant eum, omnes scripserit cum eu, elit solet albucius te sea. Etiam nonumes id sea. Parturient ultrices fermentum pede vestibulum eu curabitur consectetuer blandit porta suspendisse. Convallis facilisis montes luctus vivamus dictumst. Vivamus luctus sit magna congue. Enim ullamcorper nam massa dui donec eu eleifend mauris quisque maecenas.</p>
      <p>Metus vitae nulla pretium purus dolor suscipit vivamus velit fermentum fermentum molestie. Amet volutpat integer, nullam imperdiet. Lorem mollis metus posuere massa tempor tortor ridiculus convallis eu tortor egestas per lectus. In velit aliquam est curabitur ad ante massa ornare eu proin velit vulputate ultrices aliquet ipsum varius congue dignissim. Primis tincidunt proin laoreet conubia posuere posuere mus habitant lorem fringilla dapibus tempor curae; phasellus, magnis curae;. Nam congue primis viverra primis libero justo sollicitudin lacinia etiam dolor fusce facilisis ullamcorper morbi lacus.</p>
      <p>Nullam. A, phasellus sed faucibus rutrum cras hymenaeos, vulputate est ridiculus litora tellus tristique integer sit, morbi donec parturient class fringilla sit. Faucibus nunc nec sed. Dignissim. Hac urna. Odio sagittis, posuere taciti gravida magna eu. Orci hymenaeos ornare penatibus ut risus, habitasse. Gravida curae; iaculis, parturient fringilla eros. A Adipiscing aptent luctus habitant facilisi proin auctor volutpat dolor inceptos sem Mauris ligula massa eleifend ridiculus proin dapibus nostra. Sit luctus lacinia ultrices penatibus morbi. Nec vehicula volutpat lacus purus quisque mauris adipiscing habitasse.</p>
      <p>Kind regards,</p>
      <div class="signature" role="img" aria-label="Handwritten signature of the sender"></div>
      <p>Mr. Jed Palmer</p>
    </div>
  </div>
</body>
</html>
```